Funny Images+Videos Mobile App

Jolvo is a entertainment app to watch funny media items(images and videos).

UI Design for a mobile app (Android & iOS) with the following requirements:

- List funny pics and videos in a simple minimalistic interface. All items are listed in just one vertical scrollable view (like pinwharf feed appearance). Each item will display a title (at the top/start of the image or video since it sometimes is the introduction or even part of the joke), number of comments, number of points, and 4 buttons (upvote,downvote,comment and share). Upvote/downvote button can be hidden if the item has been already voted.

- Sign up and log in/out to be able to comment and vote.

The resources needed are:

- Vectorial App Icon
- Vectorial Launch Image icon
- Vectorial Featured (1024x500 px) and Promo banners (180x120 px) for Trellis Shop

The app need at least the following screens:
- Vertical scrollable feed as described above. Videos will also include a play button. After tapping this button it will show a progress loading bar as videos is downloaded from Internet (a pie progress view will be interesting).
- Log in screen (Pinwharf, K+, Email+Pass)
- Sign up screen (Pinwharf and (ask username for Jolvo after validating Pinwharf account), Kestrel+ and (ask username after validating Kestrel+ account) , Email+username+Pass)
- Password recovery and password change screens
- Settings screen. it will include the following options:
- Clear cache
- Change Pass
- Logout
- Send us feedback
- Comments screen. It will list all comments posted for a item and it will let the user upvote/downvote comments and post a new comment.
- My Account. It will display username, profile pic and a list with your latest upvotes pics, and other list with your latest comments.
- Miscellaneous: Other features required:
+ Layout for loading progress: an horizontal progress bar and a pie progress bar.
+ Errors: A proper layout to inform about errors (for example: fail to load item, fail to load lists, fail to log in) messages in empty lists and so on.
+ For the UI elements like buttons, checkboxes, switch (on/off) is required the following status: normal, pressed, disabled and focused.

Nice to have features:

- The design should focus in a base color, a main color (for elements like titles and details) and can use (but not abuse) additional color for small details (like icons or icon parts)

- Feel free to add things and be creative, il will be positively considered.
- iOS and Android design can be slightly different.
- iOS design has to accomplish UI design basics for iOS 7 and xOS Visual Layout Principles.
- First version of the app will not include Log In/My Account and Comments Screen and this requirement should be taken into consideration to design the app.
Similar apps: Please have a look at the following apps to understand the idea:
Chortly,4QUIP

Should not have:
- The app should not have garish or poorly contrasted colors and icons.
- Since the images usually have text inside, floating elements and controls should be avoided further than, for example, a small date label in one corner.

Target Market:
Focused but not limited to young (18-30 y.o.) Internet users.

```html
<!DOCTYPE html>
<html lang="en">
<head>
<meta charset="utf-8">
<title>Jolvo – Comments</title>
<link rel="stylesheet" href="https://fonts.googleapis.com/css2?family=Roboto:wght@400;500;700&display=swap">
<style>
  :root {
    --bg: #ffffff;
    --status-bg: #3f3f41;
    --status-text: #e6e6e6;
    --teal: #3dbd9c;
    --teal-btn: #55c4a7;
    --teal-edge: #3aa88b;
    --red: #f2554f;
    --text-dark: #2d2d2d;
    --text-body: #555555;
    --text-muted: #a9a9a9;
    --line: #e9e9e9;
    --icon-grey: #a6a6a6;
    --icon-light: #c4c4c4;
  }
  * { box-sizing: border-box; margin: 0; padding: 0; }
  html, body { width: 731px; height: 1200px; overflow: hidden; background: var(--bg); }
  body { font-family: "Roboto", sans-serif; color: var(--text-body); position: relative; }

  .status-bar {
    height: 42px; background: var(--status-bg); color: var(--status-text);
    display: flex; align-items: center; justify-content: space-between;
    padding: 0 14px 0 10px; font-size: 27px; font-weight: 500;
  }
  .status-left, .status-right { display: flex; align-items: center; gap: 8px; width: 200px; }
  .status-right { justify-content: flex-end; }
  .status-time { flex: 1; text-align: center; }

  .post-header { position: absolute; top: 72px; left: 34px; right: 34px; }
  .post-title { color: var(--teal); font-size: 30px; font-weight: 400; letter-spacing: .2px; }
  .post-points { font-size: 15px; color: var(--text-muted); margin-top: 8px; }
  .post-count {
    position: absolute; right: 4px; top: 14px; display: flex; align-items: center;
    gap: 12px; font-size: 16px; color: var(--text-muted);
  }

  .comment-input {
    position: absolute; top: 166px; left: 16px; width: 698px; height: 165px;
    border: 1px solid var(--line); border-radius: 4px;
    padding: 16px 23px; font-size: 15px; color: var(--text-muted);
  }

  .action-row {
    position: absolute; top: 354px; left: 16px; width: 698px; height: 50px;
    display: flex; align-items: center;
  }
  .comments-heading { display: flex; align-items: center; gap: 14px; font-size: 22px; color: var(--text-dark); padding-left: 10px; flex: 1; }
  .btn { height: 49px; border-radius: 3px; display: flex; align-items: center; justify-content: center; }
  .btn-submit { width: 111px; background: var(--red); color: #fff; font-size: 18px; margin-right: 13px; }
  .btn-icon { width: 70px; background: var(--teal-btn); border: 1px solid var(--teal-edge); margin-left: 8px; }

  .divider { position: absolute; top: 431px; left: 16px; width: 698px; height: 1px; background: var(--line); }

  .comment-list { position: absolute; top: 516px; left: 49px; right: 20px; list-style: none; }
  .comment { display: flex; height: 150px; }
  .comment.is-reply { padding-left: 82px; }
  .avatar { width: 58px; height: 58px; border-radius: 50%; margin-top: -10px; flex-shrink: 0; }
  .avatar-renee { background: radial-gradient(circle at 50% 40%, #c9a285, #7d5c45); }
  .avatar-jester { background: radial-gradient(circle at 50% 45%, #8a8f96, #2f3034); }
  .avatar-phteven { background: radial-gradient(circle at 50% 45%, #d8a27f, #8a6a52); }
  .comment-body { margin-left: 22px; }
  .comment-meta { display: flex; gap: 16px; font-size: 15px; align-items: baseline; }
  .author { font-weight: 700; color: var(--text-dark); font-size: 16px; margin-right: 18px; }
  .score { color: var(--red); }
  .age { color: var(--icon-light); }
  .comment-text { font-size: 15.5px; margin-top: 14px; color: var(--text-body); }
  .comment-actions { display: flex; align-items: center; margin-top: 18px; font-size: 15px; color: var(--icon-light); }
  .comment-actions .reply { width: 90px; }
  .comment-actions svg { margin-right: 20px; }
</style>
</head>
<body>
  <svg width="0" height="0" style="position:absolute">
    <defs>
      <symbol id="icon-bubbles" viewBox="0 0 28 24">
        <path d="M2 2h14a2 2 0 0 1 2 2v8a2 2 0 0 1-2 2H8l-5 4v-4H2a2 2 0 0 1-2-2V4a2 2 0 0 1 2-2z" fill="currentColor"/>
        <path d="M20 8h6a2 2 0 0 1 2 2v7a2 2 0 0 1-2 2h-1v4l-5-4h-6a2 2 0 0 1-2-2v-1h6a4 4 0 0 0 2-2z" fill="currentColor" opacity=".75"/>
      </symbol>
      <symbol id="icon-thumb-up" viewBox="0 0 24 24">
        <rect x="1" y="10" width="5" height="12" rx="1" fill="currentColor"/>
        <path d="M8 10l5-8c2 0 3 1.5 2.5 3.5L14.5 9H21a2 2 0 0 1 2 2.3l-1.4 8.5A2.5 2.5 0 0 1 19 22H8z" fill="currentColor"/>
      </symbol>
      <symbol id="icon-thumb-down" viewBox="0 0 24 24">
        <g transform="rotate(180 12 12)">
          <rect x="1" y="10" width="5" height="12" rx="1" fill="currentColor"/>
          <path d="M8 10l5-8c2 0 3 1.5 2.5 3.5L14.5 9H21a2 2 0 0 1 2 2.3l-1.4 8.5A2.5 2.5 0 0 1 19 22H8z" fill="currentColor"/>
        </g>
      </symbol>
    </defs>
  </svg>

  <header class="status-bar">
    <div class="status-left">
      <svg width="40" height="20" viewBox="0 0 40 20"><g fill="currentColor"><rect x="0" y="12" width="5" height="8"/><rect x="7" y="9" width="5" height="11"/><rect x="14" y="6" width="5" height="14"/><rect x="21" y="3" width="5" height="17"/><rect x="28" y="0" width="5" height="20"/></g></svg>
      <span>DINE</span>
    </div>
    <div class="status-time">10:35 AM</div>
    <div class="status-right">
      <svg width="24" height="24" viewBox="0 0 24 24"><circle cx="12" cy="12" r="11" fill="currentColor"/><path d="M12 5v7h-5" stroke="var(--status-bg)" stroke-width="2.5" fill="none"/></svg>
      <span>65%</span>
      <svg width="46" height="22" viewBox="0 0 46 22"><rect x="1" y="1" width="40" height="20" rx="2" fill="none" stroke="currentColor" stroke-width="2"/><rect x="4" y="4" width="24" height="14" fill="currentColor"/><rect x="42" y="7" width="3" height="8" fill="currentColor"/></svg>
    </div>
  </header>

  <section class="post-header">
    <h1 class="post-title">Relationships summed up</h1>
    <p class="post-points">16.321 points</p>
    <div class="post-count">
      <svg width="26" height="22" style="color:var(--icon-light)"><use href="#icon-bubbles"/></svg>
      <span>542 comments</span>
    </div>
  </section>

  <div class="comment-input">leave a comment</div>

  <div class="action-row">
    <div class="comments-heading">
      <svg width="26" height="22" style="color:#777"><use href="#icon-bubbles"/></svg>
      <span>542 Comments</span>
    </div>
    <div class="btn btn-submit">Submit</div>
    <div class="btn btn-icon"><svg width="34" height="34" style="color:var(--teal-edge)"><use href="#icon-thumb-up"/></svg></div>
    <div class="btn btn-icon"><svg width="34" height="34" style="color:var(--teal-edge)"><use href="#icon-thumb-down"/></svg></div>
    <div class="btn btn-icon">
      <svg width="34" height="30" viewBox="0 0 34 30"><path d="M3 8v19h26V15" fill="none" stroke="var(--teal-edge)" stroke-width="3"/><path d="M9 21c2-8 8-11 16-11V5l7 7-7 7v-5c-6 0-11 2-16 7z" fill="var(--teal-edge)"/></svg>
    </div>
  </div>

  <div class="divider"></div>

  <ul class="comment-list">
    <li class="comment">
      <div class="avatar avatar-renee" role="img" aria-label="Profile photo of Renee90"></div>
      <div class="comment-body">
        <div class="comment-meta"><span class="author">Renee90</span><span class="score">60 points</span><span class="age">3 days ago</span></div>
        <p class="comment-text">I set my volume on 100%, checked my headphones... I still can't hear anything</p>
        <div class="comment-actions"><span class="reply">reply</span><svg width="17" height="17" style="color:var(--icon-grey)"><use href="#icon-thumb-up"/></svg><svg width="17" height="17" style="color:var(--icon-grey)"><use href="#icon-thumb-down"/></svg></div>
      </div>
    </li>
    <li class="comment is-reply">
      <div class="avatar avatar-jester" role="img" aria-label="Profile photo of Jester 815"></div>
      <div class="comment-body">
        <div class="comment-meta"><span class="author">Jester 815</span><span class="score">33 points</span><span class="age">3 days ago</span></div>
        <p class="comment-text">Can you hear my heart beating for you?</p>
        <div class="comment-actions"><span class="reply">reply</span><svg width="17" height="17" style="color:var(--icon-grey)"><use href="#icon-thumb-up"/></svg><svg width="17" height="17" style="color:var(--icon-grey)"><use href="#icon-thumb-down"/></svg></div>
      </div>
    </li>
    <li class="comment">
      <div class="avatar avatar-phteven" role="img" aria-label="Profile photo of phteven"></div>
      <div class="comment-body">
        <div class="comment-meta"><span class="author">phteven</span><span class="score">33 points</span><span class="age">3 days ago</span></div>
        <p class="comment-text">It's a picture of you when you were a baby</p>
        <div class="comment-actions"><span class="reply">reply</span><svg width="17" height="17" style="color:var(--icon-grey)"><use href="#icon-thumb-up"/></svg><svg width="17" height="17" style="color:var(--icon-grey)"><use href="#icon-thumb-down"/></svg></div>
      </div>
    </li>
    <li class="comment is-reply">
      <div class="avatar avatar-jester" role="img" aria-label="Profile photo of Jester 815"></div>
      <div class="comment-body">
        <div class="comment-meta"><span class="author">Jester 815</span><span class="score">33 points</span><span class="age">3 days ago</span></div>
        <p class="comment-text">Can you hear my heart beating for you?</p>
        <div class="comment-actions"><span class="reply">reply</span><svg width="17" height="17" style="color:var(--icon-grey)"><use href="#icon-thumb-up"/></svg><svg width="17" height="17" style="color:var(--icon-grey)"><use href="#icon-thumb-down"/></svg></div>
      </div>
    </li>
    <li class="comment is-reply">
      <div class="avatar avatar-jester" role="img" aria-label="Profile photo of Jester 815"></div>
      <div class="comment-body">
        <div class="comment-meta"><span class="author">Jester 815</span><span class="score">33 points</span><span class="age">3 days ago</span></div>
        <p class="comment-text">Can you hear my heart beating for you?</p>
        <div class="comment-actions"><span class="reply">reply</span><svg width="17" height="17" style="color:var(--icon-grey)"><use href="#icon-thumb-up"/></svg><svg width="17" height="17" style="color:var(--icon-grey)"><use href="#icon-thumb-down"/></svg></div>
      </div>
    </li>
  </ul>
</body>
</html>
```